Travel Blogger Business Card for roamquill.net

I need a two-sided business card for a travel blogging website. The card should be both professional and fun at the same time. This is for the website www.roamquill.net

I don't necessarily think that the current logo on the website needs to be used on the business card but it can be. I am very flexible with ideas

Target Market(s)

Travel agencies that will be met at a conference.

Industry/Entity Type

Travel

Contact Information for Business Card

Company Name: Roam Quill.net
Name: Bertrand Olesky
Voice: +1-(345)-402-7731
Address: Coral Reach Shore, Grand Cayman, Cayman Islands
Email: ceo@roamquill.net

Colors
0592cd
0355a3
3176b5
33a6d7
85cae6
85acd3

Requirements
Must have
• Website address and name should be bigger than address, phone number, and email.

```html
<!DOCTYPE html>
<html lang="en">
<head>
<meta charset="utf-8">
<title>Roam Quill – Business Card</title>
<link rel="stylesheet" href="https://fonts.googleapis.com/css2?family=Arimo:wght@400;700&family=Bebas+Neue&display=swap">
<style>
  :root {
    --page-bg: #eceff2;
    --card-bg: #ffffff;
    --blue-deep: #3176b5;
    --blue-bright: #1a8fcf;
    --blue-mid: #33a6d7;
    --blue-pale: #85cae6;
    --ink: #111111;
    --white: #ffffff;
  }
  html, body {
    margin: 0;
    padding: 0;
    width: 1200px;
    height: 1109px;
    overflow: hidden;
    background: var(--page-bg);
  }
  .card {
    position: absolute;
    left: 260px;
    width: 680px;
    height: 406px;
    background: var(--card-bg);
    box-shadow: 0 6px 18px rgba(0,0,0,0.18);
  }
  .card--front { top: 76px; }
  .card--back { top: 612px; }
  .card svg { display: block; width: 100%; height: 100%; }

  .fill-deep { fill: var(--blue-deep); }
  .fill-bright { fill: var(--blue-bright); }
  .fill-mid { fill: var(--blue-mid); }
  .fill-pale { fill: var(--blue-pale); }
  .fill-white { fill: var(--white); }

  .brand-name {
    font-family: "Arimo", Arial, sans-serif;
    font-weight: 700;
    font-size: 15px;
    letter-spacing: 0.3px;
    fill: var(--white);
  }
  .person-name {
    font-family: "Bebas Neue", "Arial Narrow", sans-serif;
    font-size: 25px;
    letter-spacing: 0.6px;
    fill: var(--ink);
  }
  .name-rule { stroke: var(--ink); stroke-width: 1.6; }
  .contact-text {
    font-family: "Arimo", Arial, sans-serif;
    font-size: 8.6px;
    fill: var(--ink);
  }
  .icon-line { fill: none; stroke: var(--white); stroke-width: 1.4; stroke-linejoin: round; stroke-linecap: round; }
  .website {
    font-family: "Arimo", Arial, sans-serif;
    font-size: 20px;
    fill: var(--white);
  }
</style>
</head>
<body>

<section class="card card--front" aria-label="Business card front">
  <svg viewBox="0 0 544 325" xmlns="http://www.w3.org/2000/svg">
    <!-- geometric panel -->
    <polygon class="fill-deep" points="0,0 204,0 0,216"/>
    <polygon class="fill-pale" points="0,216 24,201 112,251 112,325 0,325"/>
    <polygon class="fill-bright" points="112,251 204,201 296,257 296,325 112,325"/>
    <polygon class="fill-mid" points="69,44 132,44 204,89 204,201 112,251 24,201 24,89"/>

    <!-- brand -->
    <circle class="fill-white" cx="44" cy="148" r="7"/>
    <text class="brand-name" x="57" y="153.5">ROAM QUILL</text>

    <!-- person -->
    <text class="person-name" x="522" y="64" text-anchor="end">BERTRAND OLESKY</text>
    <line class="name-rule" x1="359" y1="70" x2="522" y2="70"/>

    <!-- phone -->
    <text class="contact-text" x="485" y="200" text-anchor="end">+1-(345)-402-7731</text>
    <rect class="fill-deep" x="493" y="184" width="29" height="31"/>
    <path class="icon-line" d="M503.5 193.5 c-1.5 1 -1 4 1.5 7.5 c2.5 3.5 5 5 6.5 4 l1 -1.5 l-2.5 -2.5 l-1.5 1 c-1 -0.5 -2.5 -2.5 -3 -4 l1.2 -1.2 l-1.5 -3 z"/>

    <!-- email -->
    <text class="contact-text" x="485" y="243" text-anchor="end">ceo@roamquill.net</text>
    <rect class="fill-pale" x="493" y="227" width="29" height="31"/>
    <rect class="icon-line" x="501" y="237" width="13" height="10"/>
    <path class="icon-line" d="M501 237 l6.5 5.5 l6.5 -5.5"/>

    <!-- address -->
    <text class="contact-text" x="485" y="288" text-anchor="end">Coral Reach Shore, Grand Cayman,</text>
    <text class="contact-text" x="485" y="304" text-anchor="end">Cayman Islands</text>
    <rect class="fill-deep" x="493" y="269" width="29" height="31"/>
    <path class="icon-line" d="M507.5 293 c-3.5 -4.5 -5 -7 -5 -9.5 a5 5 0 0 1 10 0 c0 2.5 -1.5 5 -5 9.5 z"/>
    <circle class="icon-line" cx="507.5" cy="283.5" r="1.8"/>
  </svg>
</section>

<section class="card card--back" aria-label="Business card back">
  <svg viewBox="0 0 544 325" xmlns="http://www.w3.org/2000/svg">
    <polygon class="fill-deep" points="181,0 362,0 292,44 254,44"/>
    <polygon class="fill-deep" points="90,255 181,200 273,254 363,200 454,255 454,325 90,325"/>
    <polygon class="fill-mid" points="254,44 292,44 363,88 363,200 273,254 181,200 181,88"/>

    <circle class="fill-white" cx="204" cy="149" r="7"/>
    <text class="brand-name" x="217" y="154.5">ROAM QUILL</text>

    <text class="website" x="272" y="303" text-anchor="middle">www.roamquill.net</text>
  </svg>
</section>

</body>
</html>
```